Tri-fold Brochure for Law Firm

Double-sided brochure to be folded into 6 sides tri-fold brochure for an estate planning special for new parents or parents-to-be. Brochure will be placed in classes for new parents/young parents.

Target Market(s)

New Parents Aged 24-34

Industry/Entity Type

Law Firm

Font styles to use
Serif

Requirements
Must have
• The information provided in the word document.
Nice to have
• Highlight the phrase "for New Parents."
• You may use the color scheme from our website:
• http://k47.9dw.sitevaultexample.com/

```html
<!DOCTYPE html>
<html lang="en">
<head>
<meta charset="utf-8">
<title>Harlow Legal – Estate Planning Special for New Parents</title>
<link href="https://fonts.googleapis.com/css2?family=Montserrat:ital,wght@0,300;0,400;0,500;0,600;0,700;1,300&display=swap" rel="stylesheet">
<style>
:root{
  --stage:#333333;
  --paper:#ffffff;
  --brand:#bf5352;
  --brand-text:#c0504f;
  --ink:#4a4a4a;
  --ink-soft:#6a6a6a;
  --mist:#e4e4e4;
}
*{margin:0;padding:0;box-sizing:border-box}
html,body{width:1200px;height:1200px;overflow:hidden;background:var(--stage);font-family:"Montserrat",sans-serif;color:var(--ink)}
.spread{position:absolute;left:249px;width:701px;height:496px;background:var(--paper);overflow:hidden}
.spread--outside{top:78px}
.spread--inside{top:644px}
.abs{position:absolute}
.ln{display:block;white-space:nowrap;text-align:justify;text-align-last:justify}
.ln.end{text-align-last:left}
.rule{display:inline-block;vertical-align:middle;height:1px;background:var(--brand);margin-left:8px}

/* outside – attorney panel */
.attorney-band{left:38px;top:0;width:162px;height:128px;background:var(--brand)}
.attorney-photo{left:25px;top:51px}
.family-silhouette{left:75px;top:255px;width:150px;height:241px;background:linear-gradient(180deg,rgba(228,228,228,0),rgba(228,228,228,.75) 25%,rgba(228,228,228,.75));border-radius:60px 60px 0 0}
.grass{left:0;bottom:0;width:270px;height:12px;background:linear-gradient(#fff,#e6e6e6)}
.quote{left:30px;top:276px;width:174px;font-size:8.8px;font-style:italic;font-weight:300;line-height:15px;color:var(--ink)}
.quote-name{left:30px;top:413px;width:118px;font-size:9.5px;color:var(--brand-text);padding-bottom:3px;border-bottom:1px solid var(--brand)}

/* outside – contact panel */
.note-title{left:258px;top:44px;font-size:9.5px;font-weight:500;color:var(--brand-text)}
.note-list{left:254px;top:62px;width:200px;border-left:1px solid var(--brand);padding-left:10px;list-style:none}
.note-list li{font-size:9.6px;font-weight:300;line-height:15px;color:var(--brand-text);margin-bottom:5px;white-space:nowrap}
.note-list li:last-child{margin-bottom:0}
.firm-name{left:268px;top:286px;width:164px;text-align:center;font-size:11.5px;font-weight:400;color:var(--ink);padding-bottom:5px;border-bottom:1px solid var(--brand)}
.contact{left:250px;top:318px;width:200px;text-align:center;font-size:9.8px;font-weight:300;line-height:22px;color:var(--ink);white-space:nowrap}
.web-tab{left:269px;top:449px;width:163px;height:47px;background:var(--brand);color:#fff;font-size:10px;font-weight:600;display:flex;align-items:center;justify-content:center;padding-bottom:6px}

/* outside – cover panel */
.cover-band{left:467px;top:0;width:234px;height:496px;background:var(--brand)}
.cover-heart{left:440px;top:-22px}
.cover-title{left:467px;top:292px;width:234px;text-align:center;color:#fff;font-size:20px;font-weight:700;line-height:27px}
.cover-title .light{font-weight:400}
.cover-brand{left:497px;top:401px;width:176px;height:40px;border-top:1px solid #f3d9d8;border-bottom:1px solid #f3d9d8;display:flex;align-items:center;justify-content:center;gap:6px;color:#fff;font-size:10.5px;font-weight:600;letter-spacing:.6px}
.cover-brand .dot{width:7px;height:7px;border-radius:50%;background:#fff}

/* inside */
.body{position:absolute;width:189px;font-size:7.4px;font-weight:300;line-height:13.4px;letter-spacing:-.1px;color:var(--ink-soft)}
.body--mid{width:179px}
.head{position:absolute;font-size:10.6px;font-weight:500;line-height:13.6px;letter-spacing:-.1px;color:var(--brand-text);white-space:nowrap}
.pen-photo{left:-87px;top:318px}
.mother-photo{left:449px;top:-44px}
.foot-rule{left:249px;top:475px;width:338px;height:1px;background:var(--brand)}
.foot-url{left:596px;top:470px;width:76px;text-align:right;font-size:6.3px;color:var(--brand-text);white-space:nowrap}
</style>
</head>
<body>

<section class="spread spread--outside" aria-label="Brochure outside">
  <div class="abs attorney-band"></div>
  <svg class="abs attorney-photo" width="194" height="194" viewBox="0 0 194 194" role="img" aria-label="Portrait photo of the attorney">
    <defs><radialGradient id="portraitTone" cx="50%" cy="45%" r="55%"><stop offset="0" stop-color="#c9a08a"/><stop offset=".6" stop-color="#6e4a44"/><stop offset="1" stop-color="#3b3334"/></radialGradient></defs>
    <circle cx="97" cy="97" r="97" fill="#ffffff"/>
    <circle cx="97" cy="97" r="92" fill="url(#portraitTone)"/>
  </svg>
  <div class="abs family-silhouette" role="img" aria-label="Faint silhouette of parents carrying a child"></div>
  <div class="abs grass"></div>
  <p class="abs quote">
    <span class="ln">“I’ve seen first-hand the problems</span>
    <span class="ln">created when a parent dies without</span>
    <span class="ln">a will. Young parents are least likely</span>
    <span class="ln">to think about estate planning, but</span>
    <span class="ln">having a plan for a guardian is most</span>
    <span class="ln">important when your children are</span>
    <span class="ln">small. I created our estate planning</span>
    <span class="ln">special to encourage new parents to</span>
    <span class="ln end">start planning before it’s too late.”</span>
  </p>
  <div class="abs quote-name">Claire M. Harlow, Esq.</div>

  <div class="abs note-title">Please note:</div>
  <ul class="abs note-list">
    <li>New Parent Estate Planning<br>program ends 12/31/17.</li>
    <li>Special does not apply to individuals<br>with over $1 million net worth or<br>particularly complex plans.</li>
    <li>Special does not include drafting<br>trusts.</li>
    <li>Available to Maryland residents only.</li>
  </ul>
  <div class="abs firm-name">HARLOW LEGAL, LLC</div>
  <div class="abs contact">
    417 Linden Court, Suite<br>12, Towson, MD 21204<br>P: (410)-555-0148<br>F: (410)-555-0172<br>E: claire@harlow-legal.com
  </div>
  <div class="abs web-tab">www.harlow-legal.com</div>

  <div class="abs cover-band"></div>
  <svg class="abs cover-heart" width="290" height="280" viewBox="0 0 290 280" role="img" aria-label="Heart-shaped photo of a smiling family with a baby">
    <defs><linearGradient id="familyTone" x1="0" y1="0" x2="1" y2="1"><stop offset="0" stop-color="#d8c39a"/><stop offset=".5" stop-color="#d98a80"/><stop offset="1" stop-color="#3f5fa6"/></linearGradient></defs>
    <path d="M144 270 L20 150 Q-20 100 10 40 Q50 -20 110 10 Q135 25 144 50 Q153 25 178 10 Q240 -20 280 40 Q310 100 268 150 Z" fill="#ffffff"/>
    <path d="M144 256 L28 144 Q-10 98 18 44 Q54 -8 108 20 Q132 34 144 60 Q156 34 180 20 Q236 -8 272 44 Q300 98 260 144 Z" fill="url(#familyTone)"/>
  </svg>
  <h1 class="abs cover-title">Estate Planning<br>Special<br><span class="light">for</span> New Parents</h1>
  <div class="abs cover-brand"><span class="dot"></span>HARLOW LEGAL, LLC</div>
</section>

<section class="spread spread--inside" aria-label="Brochure inside">
  <h2 class="head" style="left:30px;top:34px">Why should every parent have<br>a will?<span class="rule" style="width:140px"></span></h2>
  <div class="body" style="left:30px;top:64px">
    <span class="ln">Imagine how many people love your children.</span>
    <span class="ln">Would there be a fight over who would care for</span>
    <span class="ln">your children if you passed away without leaving</span>
    <span class="ln end">instructions?</span>
    <span class="ln">Naming a guardian in your will helps avoid</span>
    <span class="ln">litigation that would cause additional stress to</span>
    <span class="ln">your children and loved ones. You can also name</span>
    <span class="ln">a back-up in the event that your first choice is</span>
    <span class="ln end">unable or unwilling to serve as guardian.</span>
  </div>

  <h2 class="head" style="left:30px;top:207px">What happens if I die in Maryland<br>without a will?<span class="rule" style="width:100px"></span></h2>
  <div class="body" style="left:30px;top:237px">
    <span class="ln">If you are married and have minor children, your</span>
    <span class="ln">spouse will inherit one half of your intestate</span>
    <span class="ln">property and your children will inherit the rest. If</span>
    <span class="ln">you have children but no spouse, your children</span>
    <span class="ln end">will inherit everything.</span>
  </div>

  <svg class="abs pen-photo" width="312" height="312" viewBox="0 0 312 312" role="img" aria-label="Close-up photo of a gold pen resting on a last will document">
    <defs><linearGradient id="penTone" x1="0" y1="0" x2="1" y2="1"><stop offset="0" stop-color="#8a6d3a"/><stop offset=".4" stop-color="#eeeae2"/><stop offset="1" stop-color="#cfcac2"/></linearGradient></defs>
    <circle cx="156" cy="156" r="156" fill="var(--brand)"/>
    <circle cx="148" cy="163" r="144" fill="url(#penTone)"/>
  </svg>

  <div class="body body--mid" style="left:249px;top:29px">
    <span class="ln">For most parents, this plan doesn’t make sense.</span>
    <span class="ln">Married people generally want their spouse to</span>
    <span class="ln">inherit all of their estate and unmarried people</span>
    <span class="ln">should have more control over how funds are</span>
    <span class="ln end">distributed to their minor children.</span>
    <span class="ln">Furthermore, Maryland law doesn’t take into</span>
    <span class="ln">account nontraditional families. For example,</span>
    <span class="ln">foster children and stepchildren that are not</span>
    <span class="ln">legally adopted will not automatically inherit a</span>
    <span class="ln end">share of your estate.</span>
    <span class="ln">You can find the complete laws of intestacy</span>
    <span class="ln">(dying without a will) in the Maryland Code of</span>
    <span class="ln end">Estates &amp; Trusts §§ 3-101 to 3-303.</span>
  </div>

  <h2 class="head" style="left:249px;top:227px">Should we prepare a will now if<br>we plan to have more children in<br>the future?<span class="rule" style="width:100px"></span></h2>
  <div class="body body--mid" style="left:249px;top:270px">
    <span class="ln">There is no reason to put off drafting a will. A</span>
    <span class="ln">will can be written to treat your children as a</span>
    <span class="ln">“class” that would include any future children</span>
    <span class="ln end">born to or adopted by you.</span>
  </div>

  <h2 class="head" style="left:249px;top:347px">What does the estate planning<br>package include?<span class="rule" style="width:72px"></span></h2>
  <div class="body body--mid" style="left:249px;top:377px">
    <span class="ln">Our estate planning package includes a will,</span>
    <span class="ln">an advance medical directive, and a power</span>
    <span class="ln">of attorney. A will names a guardian for your</span>
    <span class="ln">children and gives instructions on how to</span>
    <span class="ln">distribute your probate property at death.</span>
    <span class="ln">An advance medical directive, also known</span>
  </div>

  <svg class="abs mother-photo" width="256" height="256" viewBox="0 0 256 256" role="img" aria-label="Photo of a smiling expectant mother holding a pink rose">
    <defs><radialGradient id="motherTone" cx="45%" cy="45%" r="60%"><stop offset="0" stop-color="#8a5a40"/><stop offset=".5" stop-color="#e6dcd6"/><stop offset="1" stop-color="#f4f1ee"/></radialGradient></defs>
    <circle cx="128" cy="128" r="128" fill="var(--brand)"/>
    <circle cx="128" cy="118" r="112" fill="url(#motherTone)"/>
  </svg>

  <div class="body" style="left:482px;top:230px">
    <span class="ln">as a living will, states directions regarding your</span>
    <span class="ln">healthcare decisions in the event that you</span>
    <span class="ln">can’t make those decisions yourself. A power</span>
    <span class="ln">of attorney gives someone the ability to handle</span>
    <span class="ln end">your financial affairs during your lifetime.</span>
  </div>

  <h2 class="head" style="left:482px;top:322px">How long will the process take?</h2>
  <div class="body" style="left:482px;top:336px">
    <span class="ln">Before our first meeting, you will receive</span>
    <span class="ln">information to help you start thinking about</span>
    <span class="ln">some of the decisions we’ll make during the</span>
    <span class="ln">initial consultation which lasts approximately one</span>
    <span class="ln">hour. It takes about 2 to 3 weeks after our initial</span>
    <span class="ln">meeting to draft your documents. You will receive</span>
    <span class="ln">draft copies of your documents to review before</span>
    <span class="ln">coming in for your last appointment to sign the</span>
    <span class="ln">documents in front of witnesses and a notary.</span>
  </div>

  <div class="abs foot-rule"></div>
  <div class="abs foot-url">www.harlow-legal.com</div>
</section>

</body>
</html>
```